New Business Card

We need to refresh our business cards. We designed these ourselves and we have no graphic design experience. We would like to find a new business card design that is professional and unique. We are an auto finance company. Feel free to play with the logo, but we would like to keep the eye very present on the card. Our corporate colors are green, grey, and white.
Green - RGB - 168,215,27; HEX - #AADD22
Grey - RGB - 196,196,196; HEX - #C4C4C4
Updates
Need to upload the vector file to finalize the project. The last logo was for a jpeg that didn't stretch well.
Industry/Entity Type
Financial Service
Contact Information for Business Card
Honestly don't know...I need your help!

```html
<!DOCTYPE html>
<html lang="en">
<head>
<meta charset="utf-8">
<title>Northway Capital – Business Card</title>
<link href="https://fonts.googleapis.com/css2?family=Work+Sans:wght@400;500;600&display=swap" rel="stylesheet">
<style>
  :root {
    --backdrop: #3a332f;
    --card: #1b1b1c;
    --card-front: #161617;
    --gloss: #3a3a3c;
    --green: #aadd22;
    --grey: #c4c4c4;
    --white: #f2f2f2;
  }
  * { box-sizing: border-box; margin: 0; padding: 0; }
  html, body { width: 1200px; height: 715px; overflow: hidden; }
  body {
    background: var(--backdrop);
    font-family: "Work Sans", Arial, sans-serif;
    position: relative;
  }
  .card {
    position: absolute;
    top: 207px;
    width: 520px;
    height: 300px;
    border-radius: 4px;
    box-shadow: 0 12px 30px rgba(0,0,0,.45);
  }
  .card--front { left: 50px; background: var(--card-front); }
  .card--back { left: 630px; background: var(--card); }

  .brand {
    display: flex;
    align-items: center;
    gap: 14px;
  }
  .brand__dot { width: 44px; height: 44px; border-radius: 50%; }
  .brand__name { font-weight: 600; white-space: nowrap; }

  .card--front .brand {
    position: absolute; left: 50%; top: 50%;
    transform: translate(-50%, -50%);
  }
  .card--front .brand__dot { width: 70px; height: 70px; background: var(--gloss); }
  .card--front .brand__name { font-size: 36px; color: var(--gloss); }

  .card--back .brand {
    position: absolute; left: 30px; top: 112px;
  }
  .card--back .brand__dot { background: var(--green); }
  .card--back .brand__name { font-size: 20px; color: var(--green); }

  .divider {
    position: absolute; left: 268px; top: 70px;
    width: 2px; height: 160px; background: var(--green);
  }
  .details {
    position: absolute; left: 290px; top: 66px;
    color: var(--white);
    font-size: 13px; line-height: 1.45;
  }
  .details__name {
    color: var(--green); font-size: 20px; font-weight: 500;
    letter-spacing: .5px; line-height: 1.1;
  }
  .details__role { margin-bottom: 6px; }
  .details__address { margin-bottom: 8px; }
  .contact { list-style: none; }
  .contact li { display: flex; align-items: center; gap: 7px; }
  .contact svg { width: 10px; height: 10px; flex: none; }
  .contact .accent { color: var(--green); }
</style>
</head>
<body>
  <section class="card card--front" aria-label="Card front">
    <div class="brand">
      <span class="brand__dot"></span>
      <span class="brand__name">Northway Capital</span>
    </div>
  </section>

  <section class="card card--back" aria-label="Card back">
    <div class="brand">
      <span class="brand__dot"></span>
      <span class="brand__name">Northway Capital</span>
    </div>
    <div class="divider"></div>
    <div class="details">
      <p class="details__name">DANIEL REYES</p>
      <p class="details__role">Director</p>
      <p class="details__address">42 Harbor Lane,<br>Mill Valley, CA 94941</p>
      <ul class="contact">
        <li>
          <svg viewBox="0 0 10 10" fill="var(--green)"><path d="M2 0h2l1 2.5-1.3 1a5 5 0 0 0 2.8 2.8l1-1.3L10 6v2a2 2 0 0 1-2 2A8 8 0 0 1 0 2a2 2 0 0 1 2-2z"/></svg>
          (555)310-2400
        </li>
        <li>
          <svg viewBox="0 0 10 10" fill="none" stroke="var(--green)" stroke-width="1.4"><rect x="2.5" y=".7" width="5" height="8.6" rx="1"/></svg>
          (555)482-7719
        </li>
        <li>
          <svg viewBox="0 0 10 10" fill="none" stroke="var(--green)" stroke-width="1.2"><rect x=".6" y="2" width="8.8" height="6"/><path d="M.6 2 5 5.5 9.4 2"/></svg>
          dan@northwaycapital.com
        </li>
        <li>
          <svg viewBox="0 0 10 10" fill="none" stroke="var(--green)" stroke-width="1"><circle cx="5" cy="5" r="4.4"/><path d="M.6 5h8.8M5 .6c2 2.4 2 6.4 0 8.8M5 .6c-2 2.4-2 6.4 0 8.8"/></svg>
          <span>www.<span class="accent">northwaycapital</span>.com</span>
        </li>
      </ul>
    </div>
  </section>
</body>
</html>
```